Collage: Kunden in Coaching und Organisationsberatung

Ich brauche eine jederzeit mit herkömmlichen Programmen bearbeitbare Vorlage, um in sozialen Medien meine Kunden vorstellen zu können - damit zu erklären, wie Coaching und Organisationsberatung wirken kann. Diese Persona sollen in einer Collage mit passenden Bildern und Texten präsentiert werden können. Als grafische Orientierung kann meine Homepage https://www.plavisno.at/ dienen. Meine Farbcodes sind auf der Webseite - sprich digital RGB: Blau: #739fc7, Grün: #b8c830 und Orange: #cc610a; Im Print also CMYK: Blau: 70/20/10/0, Grün: 0/10/100/0 und Orange: 0/68/100/0; Texte sollen in folgender Länge Platz finden - diese Info dient nur zur Größenabschätzung der Platzhalter. Der Rest kann frei mit Bildern, Symbolen, ... gestaltet werden.
Textbeispiel 1:
Helga – Führungskraft mit Ambitionen und Herausforderungen
Alter: 42 Jahre
Funktion: Bereichsleiterin Finanzen in einem großen Dienstleistungsunternehmen
Lebenssituation: Verheiratet, zwei Kinder (Gymnasium, Unterstufe), Partner arbeitet als technischer Zeichner
🎯 Ziele & 🧭 Motive
• Will sich als moderne Führungskraft etablieren – mit Haltung, Vertrauen und Eigenverantwortung
• Strebt eine konstruktive, offene Kommunikation in ihrem Bereich an
• Möchte ihren Managementstil von operativer Detailarbeit hin zur strategischen Führung weiterentwickeln
• Sucht nach Balance zwischen Beruf, Familie und persönlichen Bedürfnissen
⚠️ Herausforderungen & Belastungen
• Übergang von Kollegin zu Vorgesetzter: Beziehungskonflikte und Rollenklarheit
• Kommunikationskultur im Team ist verschlossen und wenig kooperativ
• Hoher Anspruch an sich selbst – und an andere
• Rückfall in operative Aufgaben → Zeitdruck & Energieverlust
• Entscheidungsschwierigkeiten durch komplexe Abstimmungen und fehlende Klarheit über Stakeholder
• Innere Spannung zwischen Führungsanspruch und fehlendem methodischem Rüstzeug
💬 Typische Aussagen
• „Ich will nicht führen wie mein Vorgänger – das geht heute anders.“
• „Ich will, dass die Leute Verantwortung übernehmen und nicht nur ausführen.“
• „Manchmal bin ich zu ungeduldig – aber ich habe einfach keine Zeit für Umwege.“
• „Ich muss weg von der Detailarbeit – aber wie schaffe ich das wirklich?“
📌 Entwicklungsbedarfe
• Coaching zur Selbstklärung und Rollenentwicklung
• Training zu Kommunikation in Führung, Feedback- und Konfliktkultur
• Impulse zur Reflexion über Führungshaltung und Teamsteuerung
• Unterstützung im Aufbau eines kollaborativen Netzwerks innerhalb der Organisation
📣 Zielgruppenansprache (Voxtera-Kontext)
Diese Persona spricht Führungskräfte an, die:
• neu in ihrer Rolle sind (meist durch schnellen Aufstieg)
• den Willen zur Veränderung mitbringen, aber noch nicht das passende Werkzeug
• zwischen strategischem Anspruch und operativem Alltag aufgerieben werden
• Kommunikation, Führung und Selbstführung gleichzeitig lernen und leben wollen
Textbeispiel 2:
Herbert
Persona: Herbert – Fachlich stark, persönlich überfordert
Alter: 36 Jahre
Funktion: Bilanzbuchhalter in einer mittelgroßen Spedition
Position: Formal als Abteilungsleiter geführt – ohne kommunizierte Führungsverantwortung
Lebenssituation: Lebt allein, gelegentliche Beziehungserfahrungen
🎯 Ziele & 🧭 Motive
• Wünscht sich Stabilität, Struktur und fachlich saubere Arbeitsprozesse
• Möchte gute, fehlerfreie Arbeit leisten und professionell wahrgenommen werden
• Hat sich für diesen Job entschieden, um mehr Lebensqualität zu gewinnen
• Sehnt sich nach Klarheit in Rollen, Zuständigkeiten und Abläufen
• Ungeklärte Führungsrolle: Der Titel „Abteilungsleiter*“ verunsichert – es fehlt eine explizite Einordnung
• Überlastung durch chaotische Prozesse und laufende Systemumstellung
• Fehlende Unterstützung im Team – insbesondere durch eine überforderte Kollegin
• Schwierigkeiten, Grenzen zu setzen oder Klarheit einzufordern – v. a. gegenüber Führungskraft und Kolleg*innen
• Perfektionismus führt zu Überstunden, Schlafproblemen und emotionaler Erschöpfung
• Geringe Sichtbarkeit im Betrieb – kaum Kommunikation außerhalb des Büros
• Hohes Bedürfnis nach Kontrolle steht einem agilen Umfeld entgegen
💬 Typische Aussagen
• „Ich bin kein Abteilungsleiter – ich habe das nie gewollt.“
• „Ich will einfach gute Arbeit machen – aber so geht das nicht.“
• „Ich habe keine Zeit, das Chaos zu ordnen – ich bin zu sehr damit beschäftigt, es auszuhalten.“
• „Coaching? Vielleicht bringt es ja wenigstens etwas Struktur in meine Gedanken.“
📌 Entwicklungsbedarfe
• Klärung der eigenen beruflichen Rolle und Abgrenzung zur Führungsverantwortung
• Unterstützung beim Umgang mit Unklarheit und Perfektionismus
• Stärkung der Selbstführung und Kommunikation im System
• Strukturierungshilfen im Arbeitsalltag – Priorisierung, Delegation, Nein-Sagen
• Entlastung durch Reflexion – Reduktion von Selbstüberforderung
• Ermutigung zur Klärung mit Führungskraft (z. B. über ein geleitetes Gespräch oder systemisches Rollenmodell)
Diese Persona spricht Mitarbeiter*innen an, die:
• fachlich sehr kompetent, aber systemisch überfordert sind
• sich in unklaren Rollen- und Erwartungsstrukturen wiederfinden
• zwischen Anspruch und Wirklichkeit leiden
• sich nach Struktur, Sicherheit und professioneller Entlastung sehnen
• Coaching als „letzte Möglichkeit“ sehen, ihre Gedanken zu ordnen und Klarheit zu gewinnen
LG und danke für die Vorschläge

```html
<!DOCTYPE html>
<html lang="de">
<head>
<meta charset="utf-8">
<title>Persona Helga – plavisno</title>
<link href="https://fonts.googleapis.com/css2?family=Poppins:wght@300;400;600;700&display=swap" rel="stylesheet">
<style>
  :root{
    --backdrop:#efefef;
    --paper:#ffffff;
    --blue:#739fc7;
    --green:#b8c830;
    --orange:#cc610a;
    --ink:#1c1c1c;
    --white:#ffffff;
  }
  *{box-sizing:border-box;margin:0;padding:0}
  html,body{width:977px;height:1200px;overflow:hidden;background:var(--backdrop);font-family:'Poppins',sans-serif;color:var(--ink)}
  .sheet{position:absolute;left:135px;top:100px;width:707px;height:1000px;background:var(--paper);overflow:hidden}
  .band-left{position:absolute;left:0;top:473px;width:335px;height:527px;background:var(--blue)}
  .band-bottom{position:absolute;left:0;top:964px;width:707px;height:36px;background:var(--blue)}

  .brand{position:absolute;left:48px;top:66px;width:261px;text-align:center}
  .brand-name{font-weight:600;font-size:32px;letter-spacing:.5px;color:var(--ink);line-height:1}

  .profile{position:absolute;left:48px;top:130px;width:261px;height:504px;background:var(--green);border:3px solid var(--white);border-radius:131px 131px 0 0}
  .portrait{position:absolute;left:75px;top:149px;width:206px;height:206px;border-radius:50%;border:4px solid var(--white);background:radial-gradient(circle at 45% 40%,#f4f1ec 0%,#e2ddd5 60%,#cfc8bd 100%)}
  .profile-text{position:absolute;left:77px;top:384px;width:200px;color:var(--ink);font-size:12.2px;line-height:14.3px}
  .profile-name{color:var(--white);font-weight:700;font-size:12.5px;margin-bottom:7px}
  .profile-role{margin-bottom:12px}
  .profile-text strong{color:var(--white);font-weight:700}
  .profile-fact{margin-bottom:7px}

  .bullets{list-style:none;font-size:11px;line-height:13px}
  .bullets li{position:relative;padding-left:20px;margin-bottom:10.4px}
  .bullets li .badge{position:absolute;left:-2px;top:50%;transform:translateY(-50%);width:11px;height:11px}

  .section-head{position:absolute;display:flex;align-items:center;gap:9px}
  .section-icon{width:31px;height:31px;border-radius:50%;background:var(--green);display:flex;align-items:center;justify-content:center;flex:none}
  .section-title{font-weight:700;font-size:15px;line-height:17px;color:var(--orange)}

  .goals-head{left:57px;top:655px}
  .goals-title{font-weight:700;font-size:15.4px;color:var(--white)}
  .goals-title .accent{color:var(--green)}
  .goals-list{position:absolute;left:71px;top:701px;width:250px;color:var(--white)}

  .contact{position:absolute;left:57px;display:flex;align-items:center;gap:5px;color:var(--white);font-size:14.5px}
  .contact-icon{width:21px;height:21px;border-radius:50%;background:var(--green);display:flex;align-items:center;justify-content:center}
  .contact-phone{top:896px}
  .contact-web{top:924px}

  .right-list{position:absolute;left:388px;width:300px}
  .challenges-head{left:372px;top:55px}
  .challenges-list{top:98px}
  .quotes-head{left:372px;top:345px}
  .quotes-list{top:383px}
  .needs-head{left:372px;top:529px}
  .needs-list{top:569px}
  .audience-head{left:372px;top:736px}
  .audience-lead{position:absolute;left:373px;top:779px;font-weight:600;font-size:11.7px}
  .audience-list{top:799px}
</style>
</head>
<body>
<svg width="0" height="0" style="position:absolute">
  <defs>
    <symbol id="badge" viewBox="0 0 20 20">
      <path d="M10 0l2.4 2.2 3.2-.4.9 3.1 2.9 1.5-1 3.1 1 3.1-2.9 1.5-.9 3.1-3.2-.4L10 20l-2.4-2.2-3.2.4-.9-3.1-2.9-1.5 1-3.1-1-3.1 2.9-1.5.9-3.1 3.2.4z" fill="#cc610a"/>
      <path d="M6 10.2l2.6 2.6L14 7.4" fill="none" stroke="#fff" stroke-width="2" stroke-linecap="round" stroke-linejoin="round"/>
    </symbol>
  </defs>
</svg>

<main class="sheet">
  <div class="band-left"></div>
  <div class="band-bottom"></div>

  <div class="brand"><span class="brand-name">plavisno</span></div>

  <section class="profile"></section>
  <div class="portrait" role="img" aria-label="Porträtfoto der Persona"></div>
  <div class="profile-text">
    <p class="profile-name">Helga</p>
    <p class="profile-role">Führungskraft mit<br>Ambitionen und<br>Herausforderungen</p>
    <p class="profile-fact"><strong>Alter:</strong> 42 Jahre</p>
    <p><strong>Funktion:</strong></p>
    <p style="margin-top:3px">Bereichsleiterin<br>Finanzen in einem großen<br>Dienstleistungsunternehmen<br>Lebenssituation: Verheiratet,<br>zwei Kinder (Gymnasium,<br>Unterstufe), Partner arbeitet<br>als technischer Zeichner</p>
  </div>

  <div class="section-head goals-head">
    <span class="section-icon"><svg width="17" height="17" viewBox="0 0 20 20"><rect x="3" y="13" width="3" height="5" fill="#fff"/><rect x="8" y="10" width="3" height="8" fill="#fff"/><rect x="13" y="7" width="3" height="11" fill="#fff"/><circle cx="16" cy="3" r="2.2" fill="none" stroke="#fff" stroke-width="1.4"/></svg></span>
    <span class="goals-title"><span class="accent">Ziele &amp;</span> Motive</span>
  </div>
  <ul class="bullets goals-list">
    <li><svg class="badge"><use href="#badge"/></svg>Will sich als moderne Führungskraft etablieren – mit Haltung, Vertrauen und Eigenverantwortung</li>
    <li><svg class="badge"><use href="#badge"/></svg>Strebt eine konstruktive, offene Kommunikation in ihrem Bereich an</li>
    <li><svg class="badge"><use href="#badge"/></svg>Möchte ihren Managementstil von operativer Detailarbeit hin zur strategischen Führung weiterentwickeln</li>
    <li><svg class="badge"><use href="#badge"/></svg>Sucht nach Balance zwischen Beruf, Familie und persönlichen Bedürfnissen</li>
  </ul>

  <div class="contact contact-phone">
    <span class="contact-icon"><svg width="12" height="12" viewBox="0 0 20 20"><path d="M5 2l3 4-2 2c1 2.5 3.5 5 6 6l2-2 4 3-2 3C9 18 2 11 2 4z" fill="#fff"/></svg></span>
    +43 (0) 660 5521907
  </div>
  <div class="contact contact-web">
    <span class="contact-icon"><svg width="13" height="13" viewBox="0 0 20 20" fill="none" stroke="#fff" stroke-width="1.6"><circle cx="10" cy="10" r="8"/><ellipse cx="10" cy="10" rx="3.5" ry="8"/><path d="M2 10h16"/></svg></span>
    www.plavisno.at
  </div>

  <div class="section-head challenges-head">
    <span class="section-icon"><svg width="16" height="16" viewBox="0 0 20 20"><path d="M10 2l8 15H2z" fill="none" stroke="#fff" stroke-width="1.8" stroke-linejoin="round"/><path d="M10 8v4" stroke="#fff" stroke-width="1.8"/><circle cx="10" cy="14.5" r="1" fill="#fff"/></svg></span>
    <span class="section-title">Herausforderungen<br>&amp; Belastungen</span>
  </div>
  <ul class="bullets right-list challenges-list">
    <li><svg class="badge"><use href="#badge"/></svg>Übergang von Kollegin zu Vorgesetzter:<br>Beziehungskonflikte und Rollenklarheit</li>
    <li><svg class="badge"><use href="#badge"/></svg>Kommunikationskultur im Team ist<br>verschlossen und wenig kooperativ</li>
    <li><svg class="badge"><use href="#badge"/></svg>Hoher Anspruch an sich selbst – und<br>an andere</li>
    <li><svg class="badge"><use href="#badge"/></svg>Rückfall in operative Aufgaben-Zeitdruck<br>&amp; Energieverlust</li>
    <li><svg class="badge"><use href="#badge"/></svg>Entscheidungsschwierigkeiten durch<br>komplexe Abstimmungen und fehlende Klarheit<br>über Stakeholder</li>
    <li><svg class="badge"><use href="#badge"/></svg>Innere Spannung zwischen<br>Führungsanspruch und fehlendem<br>methodischem Rüstzeug</li>
  </ul>

  <div class="section-head quotes-head">
    <span class="section-icon"><svg width="14" height="16" viewBox="0 0 16 20"><rect x="1" y="1" width="14" height="18" rx="1.5" fill="#fff"/><path d="M4 6h8M4 9h8M4 12h8M4 15h5" stroke="#b8c830" stroke-width="1.3"/></svg></span>
    <span class="section-title">Typische Aussagen</span>
  </div>
  <ul class="bullets right-list quotes-list">
    <li><svg class="badge"><use href="#badge"/></svg>„Ich will nicht führen wie mein<br>Vorgänger – das geht heute anders.“</li>
    <li><svg class="badge"><use href="#badge"/></svg>„Ich will, dass die Leute Verantwortung über-<br>nehmen und nicht nur ausführen.“</li>
    <li><svg class="badge"><use href="#badge"/></svg>„Manchmal bin ich zu ungeduldig – aber ich<br>habe einfach keine Zeit für Umwege.“</li>
    <li><svg class="badge"><use href="#badge"/></svg>„Ich muss weg von der Detailarbeit – aber wie<br>schaffe ich das wirklich?“</li>
  </ul>

  <div class="section-head needs-head">
    <span class="section-icon"><svg width="17" height="17" viewBox="0 0 20 20"><rect x="3" y="11" width="3" height="6" fill="#fff"/><rect x="8.5" y="8" width="3" height="9" fill="#fff"/><rect x="14" y="4" width="3" height="13" fill="#fff"/><path d="M2 19h16" stroke="#fff" stroke-width="1.5"/></svg></span>
    <span class="section-title">Entwicklungsbedarfe</span>
  </div>
  <ul class="bullets right-list needs-list">
    <li><svg class="badge"><use href="#badge"/></svg>Coaching zur Selbstklärung<br>und Rollenentwicklung</li>
    <li><svg class="badge"><use href="#badge"/></svg>Training zu Kommunikation in Führung, Feed-<br>back- und Konfliktkultur</li>
    <li><svg class="badge"><use href="#badge"/></svg>Impulse zur Reflexion über<br>Führungshaltung und Teamsteuerung</li>
    <li><svg class="badge"><use href="#badge"/></svg>Unterstützung im Aufbau eines<br>kollaborativen Netzwerks innerhalb<br>der Organisation</li>
  </ul>

  <div class="section-head audience-head">
    <span class="section-icon"><svg width="16" height="16" viewBox="0 0 20 20" fill="none" stroke="#fff" stroke-width="1.8"><circle cx="8" cy="8" r="6"/><path d="M12.5 12.5L18 18" stroke-linecap="round"/></svg></span>
    <span class="section-title">Zielgruppenansprache<br>(Voxtera-Kontext)</span>
  </div>
  <p class="audience-lead">Diese Persona spricht Führungskräfte an, die:</p>
  <ul class="bullets right-list audience-list">
    <li><svg class="badge"><use href="#badge"/></svg>Neu in ihrer Rolle sind (meist durch schnellen<br>Aufstieg)</li>
    <li><svg class="badge"><use href="#badge"/></svg>Den Willen zur Veränderung mitbringen, aber<br>noch nicht das passende Werkzeug</li>
    <li><svg class="badge"><use href="#badge"/></svg>Zwischen strategischem Anspruch und<br>operativem Alltag aufgerieben werden</li>
    <li><svg class="badge"><use href="#badge"/></svg>Kommunikation, Führung und<br>Selbstführung gleichzeitig lernen<br>und leben wollen</li>
  </ul>
</main>
</body>
</html>
```